Book Cover

Hello!
I need someone to design a book cover with the title, subtitle and one of the photos attached.

- Title: Beyond the Grey Hours - By Corwin Ashdale
- Subtitle: A Steady Handbook for finding calm and strength after hard news.

```html
<!DOCTYPE html>
<html lang="en">
<head>
<meta charset="UTF-8">
<title>Beyond the Grey Hours — Book Cover</title>
<link rel="stylesheet" href="https://fonts.googleapis.com/css2?family=Anton&family=Oswald:wght@700&family=Open+Sans:wght@400&display=swap">
<style>
  :root {
    --page-bg: #e6e6e6;
    --paper: #f3f4f5;
    --ink-navy: #161b2e;
    --band-navy: #0e1326;
    --band-text: #f2f3f6;
    --sky: #c9dcea;
    --grass-light: #c9b27c;
    --grass-mid: #a48b55;
    --grass-dark: #6d6138;
  }
  * { box-sizing: border-box; margin: 0; padding: 0; }
  html, body {
    width: 1153px;
    height: 1200px;
    overflow: hidden;
    background: var(--page-bg);
  }
  .canvas {
    position: relative;
    width: 1153px;
    height: 1200px;
  }
  .book-cover {
    position: absolute;
    left: 196px;
    top: 30px;
    width: 760px;
    height: 1140px;
    background: var(--paper);
    overflow: hidden;
    box-shadow: 0 18px 40px rgba(0,0,0,0.18);
  }
  .cover-photo {
    position: absolute;
    left: 0;
    top: 170px;
    width: 760px;
    height: 820px;
    display: block;
  }
  .author-name {
    position: absolute;
    top: 92px;
    left: 0;
    width: 100%;
    text-align: center;
    font-family: "Oswald", sans-serif;
    font-weight: 700;
    font-size: 36px;
    letter-spacing: 0.22em;
    color: var(--ink-navy);
    text-transform: uppercase;
  }
  .book-title {
    position: absolute;
    top: 250px;
    left: 0;
    width: 100%;
    text-align: center;
    font-family: "Anton", sans-serif;
    font-weight: 400;
    font-size: 132px;
    line-height: 0.98;
    color: var(--ink-navy);
    text-transform: uppercase;
    letter-spacing: -0.005em;
  }
  .book-title span { display: block; }
  .subtitle-band {
    position: absolute;
    left: 0;
    bottom: 0;
    width: 760px;
    height: 250px;
    background: var(--band-navy);
    clip-path: polygon(0 14%, 100% 0, 100% 100%, 0 100%);
    display: flex;
    align-items: center;
    justify-content: center;
    padding: 40px 70px 0;
  }
  .subtitle {
    font-family: "Open Sans", sans-serif;
    font-weight: 400;
    font-size: 35px;
    line-height: 1.28;
    color: var(--band-text);
    text-align: center;
  }
</style>
</head>
<body>
<main class="canvas">
  <article class="book-cover">
    <svg class="cover-photo" viewBox="0 0 760 820" role="img" aria-label="Photograph of an older man in a blue jacket standing in a field of tall autumn grass and bare trees">
      <defs>
        <linearGradient id="fieldGradient" x1="0" y1="0" x2="0" y2="1">
          <stop offset="0" stop-color="var(--sky)"/>
          <stop offset="0.22" stop-color="#d8d4bd"/>
          <stop offset="0.42" stop-color="var(--grass-light)"/>
          <stop offset="0.72" stop-color="var(--grass-mid)"/>
          <stop offset="1" stop-color="var(--grass-dark)"/>
        </linearGradient>
      </defs>
      <path fill="url(#fieldGradient)" d="M0 90 L30 70 L55 88 L90 60 L120 82 L160 50 L190 76 L230 40 L262 66 L300 30 L335 58 L370 22 L402 50 L440 18 L470 44 L510 12 L545 40 L580 8 L615 34 L650 4 L690 30 L725 0 L760 20 L760 820 L0 820 Z"/>
    </svg>

    <p class="author-name">Corwin Ashdale</p>

    <h1 class="book-title">
      <span>Beyond the</span>
      <span>Grey Hours</span>
    </h1>

    <div class="subtitle-band">
      <p class="subtitle">A Steady Handbook for finding calm and strength after hard news.</p>
    </div>
  </article>
</main>
</body>
</html>
```